Fahrzeugbeschriftung für technischen Dienstleister
... obwohl erst unmittelbar vor Projektende das Design eingereicht wurde, ist dann in kürzester Zeit ein für unseren Geschmack sehr gutes Ergebnis entstanden, sehr professionelle Arbeitsweise und Kommunikation, die Vorgaben aus dem Briefing waren schon im ersten Vorschlag umgesetzt und mußten nur noch leicht verändert werden ... Vielen Dank!
Zielgruppe
Wir sind ein technischer Dienstleister und betreuen vor allem Industriekunden und das Handwerk.
Im Vordergrund stehen der Verkauf / Wartung / Reparatur von Kompressoren und Zubehör.
Aufgabenstellung
Wir möchten unser neues Service - Fahrzeug (KV Trabolt, mittellang/mittelhoch, Farbe stahlblau) beschriften lassen -
Das Logo der Firma existiert bereits und sollte daher nicht wesentlich verändert werden, eine Trennung der Worte ist kein Problem, das 'm' im Logo kann auch gern allein verwendet werden.
Die Darstellung im allgemeinen sollte klassisch/seriös sein und trotzdem modern und frisch wirken. Eventuell ist die Einbindung eines gestalterischen Elements wie z.Bsp. ein Manometer, Spiralschlauch o.ä. möglich.
Die beiden Hecktüren und die Schiebetür sind mit Fenster, werden aber mit Folie abgedunkelt beklebt.
Unsere Homepage für weitere evtl. Infos: www.holbinger-drucklufttechnik.de
Vielen Dank im voraus für Ihr Interesse!

```html
<!DOCTYPE html>
<html lang="de">
<head>
<meta charset="utf-8">
<title>Holbinger Drucklufttechnik – Fahrzeugbeschriftung</title>
<link rel="stylesheet" href="https://fonts.googleapis.com/css2?family=Josefin+Sans:wght@700&display=swap">
<style>
  :root {
    --brand-blue: #1f5fa6;
    --body-white: #f2f2f2;
    --trim-dark: #2a2a2a;
    --glass: #a4a4a4;
    --tyre: #1c1c1c;
    --hub: #8c8c8c;
    --light-red: #b3262d;
    --page: #ffffff;
  }
  html, body {
    margin: 0;
    padding: 0;
    width: 1200px;
    height: 1176px;
    overflow: hidden;
    background: var(--page);
  }
  .wrap-sheet { display: block; width: 1200px; height: 1176px; }
  .van-body { fill: var(--body-white); stroke: #d4d4d4; stroke-width: 2; }
  .side-window { fill: var(--glass); stroke: var(--trim-dark); stroke-width: 6; }
  .blue-band { fill: var(--brand-blue); }
  .trim-stripe { fill: var(--trim-dark); }
  .tail-light { fill: var(--light-red); }
  .tyre { fill: var(--tyre); }
  .hub { fill: var(--hub); stroke: #5a5a5a; stroke-width: 3; }
  .brand-dot { fill: var(--brand-blue); }
  .brand-name, .brand-line, .phone-number, .web-address {
    font-family: "Josefin Sans", sans-serif;
    font-weight: 700;
  }
  .brand-name { fill: var(--brand-blue); font-size: 74px; }
  .brand-line { fill: var(--brand-blue); font-size: 40px; }
  .phone-number { fill: var(--body-white); font-size: 40px; letter-spacing: 2px; }
  .phone-icon { fill: var(--body-white); }
  .web-address { fill: var(--body-white); font-size: 18px; letter-spacing: 2.5px; }
</style>
</head>
<body>
<svg class="wrap-sheet" viewBox="0 0 1200 1176" xmlns="http://www.w3.org/2000/svg">
  <defs>
    <clipPath id="body-shape">
      <path id="body-outline" d="M40,330 Q45,292 110,272 L300,232 Q350,132 430,82 Q470,42 530,32 L1110,28 Q1142,30 1146,72 L1150,440 L1165,445 L1165,462 L1100,466 L1000,470 A80,80 0 0 0 850,470 L300,470 A80,80 0 0 0 130,470 L58,470 Q36,460 38,420 Z"/>
    </clipPath>
    <g id="van-side">
      <use href="#body-outline" class="van-body"/>
      <g clip-path="url(#body-shape)">
        <path class="blue-band" d="M60,388 Q300,300 620,268 Q800,252 1160,250 L1160,480 L40,480 Z"/>
        <path class="van-body" style="stroke:none" d="M40,372 Q130,338 200,340 Q250,345 285,380 L285,480 L40,480 Z"/>
        <rect class="trim-stripe" x="0" y="388" width="1200" height="36"/>
        <rect class="trim-stripe" x="0" y="448" width="1200" height="40"/>
        <rect class="trim-stripe" x="30" y="388" width="150" height="100"/>
        <rect class="trim-stripe" x="1110" y="388" width="60" height="100"/>
      </g>
      <path class="side-window" d="M300,250 L360,120 L470,118 L470,245 Z"/>
      <rect class="tail-light" x="1128" y="262" width="20" height="110" rx="3"/>
      <circle class="tyre" cx="215" cy="470" r="76"/>
      <circle class="hub" cx="215" cy="470" r="42"/>
      <circle class="tyre" cx="925" cy="470" r="76"/>
      <circle class="hub" cx="925" cy="470" r="42"/>
    </g>
    <path id="handset" d="M6,0 C2,0 0,4 0,8 C0,22 10,34 22,38 C26,39 30,37 31,33 L32,29 L24,24 L20,28 C14,25 10,19 9,13 L13,10 L9,1 Z"/>
  </defs>

  <!-- Fahrerseite -->
  <g class="van van-left" transform="translate(0,10)">
    <use href="#van-side"/>
    <circle class="brand-dot" cx="610" cy="140" r="95"/>
    <text class="brand-name" x="724" y="172">holbinger</text>
    <text class="brand-line" x="724" y="220">drucklufttechnik</text>
    <use href="#handset" class="phone-icon" transform="translate(372,328)"/>
    <text class="phone-number" x="412" y="364">05231 / 48 27 16</text>
    <text class="web-address" x="565" y="443" text-anchor="middle">WWW.HOLBINGER-DRUCKLUFTTECHNIK.DE</text>
  </g>

  <!-- Beifahrerseite -->
  <g class="van van-right" transform="translate(0,600)">
    <use href="#van-side" transform="translate(1200,0) scale(-1,1)"/>
    <circle class="brand-dot" cx="235" cy="150" r="95"/>
    <text class="brand-name" x="348" y="182">holbinger</text>
    <text class="brand-line" x="348" y="230">drucklufttechnik</text>
    <use href="#handset" class="phone-icon" transform="translate(408,328)"/>
    <text class="phone-number" x="448" y="364">05231 / 48 27 16</text>
    <text class="web-address" x="640" y="443" text-anchor="middle">WWW.HOLBINGER-DRUCKLUFTTECHNIK.DE</text>
  </g>
</svg>
</body>
</html>
```